Company Website for Vortel Insight, an open source data analytics company focused on relationship and li

I need a company/brand website for our new startup, Vortel Insight LLC. We are a company focused on using life pattern analysis techniques, looking at relationships and how relationships, attributes, and activity cluster to infer aggregate information about individuals and groups. Our focus is on improving the digital advertising market.

We have a company logo which I will upload shortly.

Target Market(s)

Digital Advertising

Number of Pages Required

3 page

Font styles to use
Sans Serif

Requirements
Must have
• An main page, about us, contact page.
Nice to have
• Vortel Insight relies on state of the art analytics applied to a the digital marketing space. While it is heavy in science, we also understand the art of influence. The website should have a scientific edge but also a flair that illustrates our focus on applying the hard science and analytics to influencing the behavior of people.

```html
<!DOCTYPE html>
<html lang="en">
<head>
<meta charset="utf-8">
<title>Vortel Insight — Digital Advertising Analytics</title>
<link rel="stylesheet" href="https://fonts.googleapis.com/css2?family=Montserrat:wght@400;500;600;700&display=swap">
<style>
  :root {
    --ink-dark: #1c1d1f;
    --panel-dark: #26272a;
    --panel-mid: #303135;
    --brand-blue: #1f74c8;
    --brand-blue-deep: #1a5fa6;
    --accent-orange: #f28c1e;
    --text-light: #ffffff;
    --text-muted: #b9bcc2;
    --page-bg: #f4f5f7;
  }
  * { box-sizing: border-box; margin: 0; padding: 0; }
  html, body { width: 1200px; height: 1200px; overflow: hidden; background: var(--page-bg); }
  body { font-family: "Montserrat", sans-serif; color: var(--text-light); }
  .site { width: 1200px; height: 1200px; display: flex; flex-direction: column; background: var(--ink-dark); }

  /* Hero */
  .hero { position: relative; height: 380px; overflow: hidden; }
  .hero-photo { position: absolute; inset: 0; background: linear-gradient(100deg, #2b2c30 0%, #4a4640 45%, #3a3833 70%, #232427 100%); }
  .hero-shade { position: absolute; inset: 0; background: rgba(20,20,22,.45); }
  .nav { position: relative; display: flex; align-items: center; justify-content: space-between; padding: 24px 70px; }
  .brand { display: flex; align-items: center; gap: 10px; font-weight: 700; font-size: 22px; color: var(--brand-blue); }
  .brand-mark { width: 14px; height: 14px; background: var(--brand-blue); }
  .nav-links { display: flex; gap: 26px; list-style: none; font-size: 12px; font-weight: 500; align-items: center; }
  .nav-links .active { border-top: 2px solid var(--brand-blue); padding-top: 4px; }
  .nav-search { width: 18px; height: 18px; border-radius: 50%; background: var(--brand-blue); }
  .hero-copy { position: relative; padding: 60px 0 0 130px; }
  .hero-kicker { display: inline-block; border: 1px solid #fff; padding: 6px 12px; font-size: 12px; font-weight: 600; letter-spacing: .5px; }
  .hero-title { font-size: 36px; font-weight: 700; line-height: 1.25; margin-top: 14px; max-width: 760px; letter-spacing: .5px; }
  .hero-btn { display: inline-block; margin-top: 16px; background: var(--brand-blue); padding: 9px 18px; font-size: 11px; font-weight: 700; letter-spacing: .5px; }
  .hero-arrow { position: absolute; top: 215px; font-size: 28px; font-weight: 400; }
  .hero-arrow.prev { left: 60px; } .hero-arrow.next { right: 60px; }
  .hero-dots { position: absolute; bottom: 30px; left: 50%; display: flex; gap: 6px; transform: translateX(-50%); }
  .hero-dots span { width: 8px; height: 8px; border-radius: 50%; background: #fff; opacity: .5; }
  .hero-dots span.on { opacity: 1; }

  /* Section heads */
  .section-title { text-align: center; font-size: 22px; font-weight: 500; letter-spacing: 1px; }
  .section-sub { text-align: center; font-size: 12px; color: var(--text-muted); margin-top: 6px; }

  /* About */
  .about { height: 262px; background: var(--panel-dark); padding: 20px 70px 0; }
  .about-tabs { display: flex; gap: 0; margin-top: 14px; font-size: 11px; color: var(--text-muted); border-bottom: 1px solid #3c3d42; }
  .about-tabs li { list-style: none; padding: 8px 22px; }
  .about-tabs li.current { color: #fff; border-bottom: 2px solid var(--brand-blue); }
  .about-body { display: flex; gap: 36px; margin-top: 18px; }
  .about-image { width: 380px; height: 138px; background: linear-gradient(180deg, #9fb2c6 0%, #6a7f96 55%, #34465a 100%); }
  .about-text h3 { font-size: 18px; font-weight: 600; letter-spacing: .5px; }
  .about-text p { font-size: 12px; line-height: 1.7; color: var(--text-muted); margin-top: 10px; max-width: 560px; }

  /* Team */
  .team { height: 262px; background: var(--ink-dark); padding: 20px 70px 0; }
  .team-grid { display: flex; gap: 20px; margin-top: 16px; }
  .member { flex: 1; background: var(--panel-mid); display: flex; }
  .member-photo { width: 110px; height: 160px; background: linear-gradient(180deg, #5a5c61 0%, #2d2e31 100%); position: relative; flex-shrink: 0; }
  .member-photo::after { content: ""; position: absolute; bottom: -9px; left: 46px; width: 18px; height: 18px; border-radius: 50%; background: var(--brand-blue); border: 2px solid #fff; }
  .member-info { padding: 18px 12px; }
  .member-info h4 { font-size: 11px; font-weight: 600; letter-spacing: .5px; }
  .member-info hr { border: 0; border-top: 1px solid #777; width: 24px; margin: 8px 0; }
  .member-info p { font-size: 10px; line-height: 1.6; color: var(--text-muted); }
  .member.featured { background: var(--brand-blue); }
  .member.featured p { color: #e4eefa; }

  /* Banner */
  .banner { height: 120px; background: linear-gradient(90deg, var(--brand-blue-deep), var(--brand-blue)); text-align: center; padding-top: 24px; }
  .banner-name { font-size: 14px; font-weight: 600; letter-spacing: 1px; }
  .banner-line { font-size: 16px; font-weight: 600; letter-spacing: 1px; margin-top: 4px; }
  .banner-btn { display: inline-block; margin-top: 12px; border: 1px solid #fff; padding: 4px 16px; font-size: 9px; font-weight: 600; }

  /* Analytics */
  .analytics { flex: 1; background: var(--panel-dark); padding-top: 18px; }
  .analytics-sub { font-style: italic; }
  .analytics-row { display: flex; margin-top: 16px; height: 98px; }
  .analytics-image { width: 500px; background: linear-gradient(90deg, #7b8794 0%, #c9d3de 50%, #5f6b78 100%); }
  .analytics-text { flex: 1; background: var(--brand-blue); padding: 22px 40px; font-size: 13px; line-height: 1.7; }
</style>
</head>
<body>
<main class="site">

  <header class="hero">
    <div class="hero-photo" role="img" aria-label="Photo of a smiling businessman in a suit holding a cup at his laptop"></div>
    <div class="hero-shade"></div>
    <nav class="nav">
      <div class="brand"><span class="brand-mark"></span>Vortel Insight</div>
      <ul class="nav-links">
        <li class="active">Home</li><li>About us</li><li>Our Team</li><li>Our Products</li><li>Blog</li><li>Contact</li><li class="nav-search"></li>
      </ul>
    </nav>
    <div class="hero-copy">
      <span class="hero-kicker">THE MOST ADVANCED PULL-UP SUSPENSIONS</span>
      <h1 class="hero-title">IMPROVING THE DIGITAL ADVERTISING MARKET</h1>
      <span class="hero-btn">OUR PRODUCTS</span>
    </div>
    <span class="hero-arrow prev">‹</span>
    <span class="hero-arrow next">›</span>
    <div class="hero-dots"><span></span><span class="on"></span><span></span></div>
  </header>

  <section class="about">
    <h2 class="section-title">ABOUT US</h2>
    <ul class="about-tabs">
      <li class="current">Our Story</li><li>Mission &amp; Vision</li><li>Company Values</li>
    </ul>
    <div class="about-body">
      <div class="about-image" role="img" aria-label="Photo of a city skyline across the water"></div>
      <div class="about-text">
        <h3>DIGITAL ADVERTISING MARKET</h3>
        <p>We map how relationships, attributes and activity cluster across audiences, turning life pattern signals into aggregate insight that helps advertisers reach groups with more precision and less waste.</p>
      </div>
    </div>
  </section>

  <section class="team">
    <h2 class="section-title">OUR TEAM</h2>
    <p class="section-sub">Morbi leo risus, porta ac consectetur ac, vestibulum at eros.</p>
    <div class="team-grid">
      <article class="member">
        <div class="member-photo" role="img" aria-label="Portrait of team member Dario Velt"></div>
        <div class="member-info"><h4>DARIO VELT</h4><hr><p>Shapes clustering models that reveal how audiences connect.</p></div>
      </article>
      <article class="member featured">
        <div class="member-photo" role="img" aria-label="Portrait of team member Elias Marr"></div>
        <div class="member-info"><h4>ELIAS MARR</h4><hr><p>Leads pattern research across social and activity data.</p></div>
      </article>
      <article class="member">
        <div class="member-photo" role="img" aria-label="Portrait of a team member with glasses"></div>
        <div class="member-info"><h4>TEAM MEMBER</h4><hr><p>Builds open source tools for large scale signal analysis.</p></div>
      </article>
      <article class="member">
        <div class="member-photo" role="img" aria-label="Portrait of a team member"></div>
        <div class="member-info"><h4>TEAM MEMBER</h4><hr><p>Turns analytic findings into clear campaigns for clients.</p></div>
      </article>
    </div>
  </section>

  <section class="banner">
    <p class="banner-name">VORTEL INSIGHT</p>
    <p class="banner-line">RELIES ON STATE OF THE ART ANALYTICS</p>
    <span class="banner-btn">BUY NOW</span>
  </section>

  <section class="analytics">
    <h2 class="section-title">ANALYTICS</h2>
    <p class="section-sub analytics-sub">simply dummy text of the printing and typesetting</p>
    <div class="analytics-row">
      <div class="analytics-image" role="img" aria-label="Photo of a laptop showing analytics bar charts on a desk"></div>
      <p class="analytics-text">It is a long established fact that a reader will be distracted by the readable content of a page when looking at its layout.</p>
    </div>
  </section>

</main>
</body>
</html>
```